Business Card Design - Law Firm

We are a boutique law firm located near the beach in Manly, Australia. We have recently had a new logo designed and are revamping our business cards with the new logo.

We have recently had a business card design done for us but are not entirely happy with it. We are looking for something modern, simplistic but striking. We would like to see multiple designs.

We have attached a word document which includes our new logo and the current business card design which we are looking at moving away from.

We would like the business cards to be double sided. We would like the design to include something which we can print in gloss colour when we send it to the business card printers.

```html
<!DOCTYPE html>
<html lang="en">
<head>
<meta charset="utf-8">
<title>Harlow &amp; Partners Lawyers – Business Card</title>
<link href="https://fonts.googleapis.com/css2?family=Montserrat:wght@400;500&family=Roboto:wght@400;700&display=swap" rel="stylesheet">
<style>
  :root {
    --backdrop: #c8c8c8;
    --navy-deep: #1e3470;
    --navy-light: #4b6aa1;
    --navy-text: #1d2f6a;
    --ink: #1f1f1f;
    --gold: #a8926a;
    --paper: #f3f3f4;
    --white: #ffffff;
  }
  * { margin: 0; padding: 0; box-sizing: border-box; }
  html, body { width: 1200px; height: 576px; overflow: hidden; }
  body { background: var(--backdrop); position: relative; font-family: "Roboto", Arial, sans-serif; }

  .card {
    position: absolute;
    top: 138px;
    width: 484px;
    height: 293px;
    border-radius: 12px;
    overflow: hidden;
  }
  .card--front { left: 82px; background: linear-gradient(200deg, var(--navy-light) 0%, var(--navy-deep) 75%); color: var(--white); }
  .card--back { left: 602px; width: 480px; background: var(--paper); }

  .front-name {
    position: absolute; left: 0; right: 0; top: 114px;
    text-align: center;
    font-family: "Montserrat", Arial, sans-serif; font-weight: 400;
    font-size: 29px; letter-spacing: 1.5px; color: #e8ecf4;
  }
  .front-tag {
    position: absolute; left: 0; right: 0; top: 157px;
    text-align: center;
    font-family: "Montserrat", Arial, sans-serif; font-weight: 400;
    font-size: 15px; letter-spacing: 11px; padding-left: 11px; color: #e8ecf4;
  }
  .front-web {
    position: absolute; left: 0; right: 0; top: 259px;
    text-align: center; font-size: 13px; letter-spacing: 0.6px; color: #c9d2e4;
  }

  .brand {
    position: absolute; left: 23px; width: 200px; top: 90px;
    text-align: center; color: var(--ink);
    font-family: "Montserrat", Arial, sans-serif; font-weight: 500;
  }
  .brand-dot { width: 52px; height: 52px; border-radius: 50%; background: var(--navy-text); margin: 0 auto 22px; }
  .brand-name { font-size: 16px; letter-spacing: 1px; }
  .brand-tag { font-size: 10px; letter-spacing: 8px; padding-left: 8px; margin-top: 3px; }

  .contact { position: absolute; left: 247px; top: 56px; color: var(--ink); }
  .contact-name { font-weight: 700; font-size: 21px; color: var(--navy-text); line-height: 26px; }
  .contact-role { font-size: 12.5px; margin-top: 2px; }
  .contact-address { font-size: 13px; line-height: 18px; margin-top: 20px; }
  .contact-lines { list-style: none; margin-top: 6px; font-size: 13px; line-height: 18px; }
  .contact-lines li { display: flex; align-items: center; margin-left: 6px; }
  .contact-lines svg { width: 11px; height: 11px; margin-right: 9px; fill: var(--navy-text); }

  .back-band { position: absolute; left: 0; bottom: 0; width: 480px; height: 38px; }
  .back-web {
    position: absolute; left: 247px; bottom: 12px;
    font-size: 13px; color: var(--white); letter-spacing: 0.3px;
  }
</style>
</head>
<body>
  <section class="card card--front">
    <div class="front-name">Harlow &amp; Partners</div>
    <div class="front-tag">LAWYERS</div>
    <div class="front-web">www.harlowandpartners.com.au</div>
  </section>

  <section class="card card--back">
    <div class="brand">
      <div class="brand-dot"></div>
      <div class="brand-name">Harlow &amp; Partners</div>
      <div class="brand-tag">LAWYERS</div>
    </div>

    <div class="contact">
      <div class="contact-name">Maya Ellison</div>
      <div class="contact-role">Managing Director</div>
      <div class="contact-address">Suite 3, 8 Corella Street<br>Tarrow NSW 2184</div>
      <ul class="contact-lines">
        <li><svg viewBox="0 0 12 12"><path d="M1 4.5C1 2.5 3.5 1.5 6 1.5s5 1 5 3l-2.3.6-.5-1.4H3.8l-.5 1.4z"/><rect x="2.5" y="5.5" width="7" height="5" rx="1"/></svg>(02) 9000 4182</li>
        <li><svg viewBox="0 0 12 12"><path d="M1 4.5C1 2.5 3.5 1.5 6 1.5s5 1 5 3l-2.3.6-.5-1.4H3.8l-.5 1.4z"/><rect x="2.5" y="5.5" width="7" height="5" rx="1"/></svg>(02) 9000 4183</li>
        <li><svg viewBox="0 0 12 12"><path d="M0.5 2.5h11v7h-11z M0.5 2.5l5.5 4 5.5-4" stroke="#fff" stroke-width="0.8"/></svg>maya.ellison@harlowlaw.com.au</li>
      </ul>
    </div>

    <svg class="back-band" viewBox="0 0 480 38" preserveAspectRatio="none" aria-hidden="true">
      <defs>
        <linearGradient id="band-blue" x1="0" x2="1" y1="0" y2="0">
          <stop offset="0" stop-color="#4a68a6"/>
          <stop offset="1" stop-color="#1e3470"/>
        </linearGradient>
      </defs>
      <rect x="0" y="29" width="200" height="9" fill="var(--gold)"/>
      <path d="M210 0H480V38H192L202 6Q204 0 210 0Z" fill="url(#band-blue)"/>
    </svg>
    <div class="back-web">www.harlowandpartners.com.au</div>
  </section>
</body>
</html>
```